Label designs for a new company manufacturing food supplements bottles and containers

The design must reflect SPIRITUAL as well as PHYSICAL THERAPEUTIC BENEFITS ,Our company BRIGHTWATER HERBALIST produces Food Supplements products line. Such as vitamins, herbs, super foods,alkalizing , weight loss and amino acids these products are made of , pills, capsules, powders and liquids. The containers are of different sizes , small , medium and large . We need a contemporary label design that represents alternative approaches to physical and spiritual healing . Labels should exude trust worthiness, character, and quality to achieve optimum customer confidence.

Target Market(s)

People of age 25 & up , 50% female 50% Male

Industry/Entity Type

Alternative Medicine

Font styles to use
Serif

Requirements
Must have
• name of company, name of product , slogan or short description for people to understand what the product is all about . supplement facts, ingredient list, directions, statements , place of production, expiration and lot numbers.
Nice to have
• Easily recognizable corporate identity for optimum brand identification.
Should not have
• Playfulness

```html
<!DOCTYPE html>
<html lang="en">
<head>
<meta charset="utf-8">
<title>Brightwater Herbalist – Fish Oil Omega-3 Label</title>
<link rel="stylesheet" href="https://fonts.googleapis.com/css2?family=Tinos:wght@400;700&display=swap">
<style>
  :root {
    --backdrop: #f2f2f2;
    --label-white: #ffffff;
    --brand-green: #6fae2c;
    --brand-green-light: #a6d04a;
    --band-orange: #e28f10;
    --band-gold: #f6bd1c;
    --band-yellow: #fbd43a;
    --ink: #161310;
  }
  * { margin: 0; padding: 0; box-sizing: border-box; }
  html, body {
    width: 1200px;
    height: 1200px;
    overflow: hidden;
    background: var(--backdrop);
    font-family: "Tinos", "Times New Roman", serif;
    color: var(--ink);
  }
  .label {
    position: absolute;
    left: 150px;
    top: 150px;
    width: 900px;
    height: 900px;
    background: var(--label-white);
    overflow: hidden;
    box-shadow: 0 2px 10px rgba(0,0,0,0.08);
  }
  .brand {
    position: absolute;
    left: 0;
    right: 0;
    top: 110px;
    display: flex;
    align-items: center;
    justify-content: center;
    gap: 14px;
  }
  .brand-dot {
    width: 26px;
    height: 26px;
    border-radius: 50%;
    background: var(--brand-green);
  }
  .brand-name {
    font-size: 40px;
    font-weight: 700;
    letter-spacing: 2px;
    color: var(--brand-green);
  }
  .band {
    position: absolute;
    left: 0;
    top: 220px;
    width: 900px;
    height: 680px;
  }
  .band svg { display: block; width: 100%; height: 100%; }
  .product {
    position: absolute;
    left: 56px;
    top: 330px;
  }
  .product-kind {
    font-size: 54px;
    line-height: 1;
    letter-spacing: 1px;
  }
  .product-name {
    font-size: 112px;
    line-height: 1;
    margin-top: 6px;
    letter-spacing: 1px;
  }
  .product-strength {
    display: flex;
    align-items: center;
    gap: 10px;
    margin-top: 2px;
  }
  .strength-rule {
    width: 230px;
    height: 3px;
    background: var(--ink);
    margin-left: 20px;
  }
  .strength-value {
    font-size: 46px;
    line-height: 1;
  }
  .benefit {
    display: inline-block;
    margin-top: 30px;
    padding: 4px 14px;
    border: 2px solid var(--ink);
    font-size: 32px;
  }
  .count {
    margin-top: 38px;
    font-size: 38px;
  }
  .category {
    margin-top: 18px;
    font-size: 30px;
    line-height: 1.05;
  }
</style>
</head>
<body>
  <main class="label">
    <div class="brand">
      <span class="brand-dot"></span>
      <span class="brand-name">BRIGHTWATER HERBALIST</span>
    </div>

    <div class="band" role="img" aria-label="Warm orange and golden band with soft decorative swirl motif">
      <svg viewBox="0 0 900 680" preserveAspectRatio="none" aria-hidden="true">
        <defs>
          <radialGradient id="band-glow" cx="0.5" cy="0.55" r="0.7">
            <stop offset="0" stop-color="var(--band-yellow)"/>
            <stop offset="0.5" stop-color="var(--band-gold)"/>
            <stop offset="1" stop-color="var(--band-orange)"/>
          </radialGradient>
          <linearGradient id="swoosh" x1="0" y1="0" x2="1" y2="0">
            <stop offset="0" stop-color="var(--brand-green)"/>
            <stop offset="1" stop-color="var(--brand-green-light)"/>
          </linearGradient>
        </defs>
        <path d="M0 48 C 300 44, 620 30, 900 0 L 900 680 L 0 680 Z" fill="url(#swoosh)"/>
        <path d="M0 62 C 300 58, 620 46, 900 18 L 900 680 L 0 680 Z" fill="url(#band-glow)"/>
      </svg>
    </div>

    <section class="product">
      <p class="product-kind">FISH OIL</p>
      <h1 class="product-name" style="font-weight:400">OMEGA-3</h1>
      <div class="product-strength">
        <span class="strength-rule"></span>
        <span class="strength-value">1000mg</span>
      </div>
      <p class="benefit">Heart Health*</p>
      <p class="count">60 Softgels</p>
      <p class="category">Dietary<br>Supplement</p>
    </section>
  </main>
</body>
</html>
```